I need to refresh my meeting minutes pages (2 of them)

I have 2 pages that need to be modernized with a new look and feel. I have attached the 2 pages that need the refresh. I am okay with one page submissions as long as the winner is willing to add the second page before payment :-) Any questions please let me know. The logo on the page is not ours but a sample of what client may give us.

```html
<!DOCTYPE html>
<html lang="en">
<head>
<meta charset="utf-8">
<title>Regular Meeting Agenda</title>
<link rel="stylesheet" href="https://fonts.googleapis.com/css2?family=Open+Sans:wght@400;600&display=swap">
<style>
:root{
  --green:#0b6a2c;
  --green-dark:#085522;
  --red:#d22a2a;
  --gold:#e8b21c;
  --ink:#333;
  --muted:#8a9096;
  --faint:#a9adb2;
  --line:#d5dadf;
  --page:#f3f6f9;
  --side:#eef1f5;
  --white:#fff;
}
*{box-sizing:border-box;margin:0;padding:0}
html,body{width:1200px;height:675px;overflow:hidden}
body{position:relative;background:var(--page);font-family:"Open Sans",sans-serif;color:var(--ink)}
.abs{position:absolute}
.topbar{left:0;top:0;width:1200px;height:50px;background:var(--white);border-bottom:1px solid #e3e6ea}
.brand{left:8px;top:6px;font-size:30px;font-weight:400;color:var(--green);letter-spacing:1px;line-height:36px}
.nav a{position:absolute;top:17px;font-size:13px;color:#333;text-decoration:none;letter-spacing:.4px}
.nav .active::after{content:"";position:absolute;left:-13px;right:-13px;top:28px;height:3px;background:var(--green)}
.sidebar{left:0;top:50px;width:313px;height:625px;background:#f6f7f9}
.divider{left:313px;top:50px;width:10px;height:625px;background:#eceef1}
.search{left:9px;top:60px;width:289px;height:32px;background:var(--white);border:1px solid #e1e4e8;font-size:12px;color:var(--muted);padding:7px 0 0 32px}
.search svg{position:absolute;left:9px;top:8px}
.featured{left:9px;top:101px;width:289px;height:31px;background:var(--green);color:#fff;font-size:13px;padding:6px 10px}
.featured span{position:absolute;right:11px;top:5px}
.featured-list{left:9px;top:132px;width:289px;height:170px;background:var(--side)}
.calendar{left:10px;top:318px;width:289px;height:295px;background:#f1f1f2;box-shadow:0 2px 8px rgba(0,0,0,.2)}
.year{left:0;width:289px;top:22px;text-align:center;font-size:22px;color:var(--faint)}
.months{left:0;top:64px;width:289px;height:25px;background:var(--green);color:#dfe9e2;font-size:9px}
.months span{position:absolute;top:6px}
.months .cur{font-size:12px;font-weight:600;color:#fff;top:4px}
.dow span,.days span{position:absolute;width:30px;margin-left:-15px;text-align:center}
.dow span{top:108px;font-size:12px;color:#333}
.days span{font-size:10px;color:var(--faint)}
.days .sel{width:20px;height:20px;margin-left:-10px;border-radius:50%;background:var(--green);color:#fff;font-weight:600;line-height:20px}
.dot{position:absolute;width:3px;height:3px;border-radius:50%}
.legend{font-size:9px;color:#777}
.legend .dot{width:8px;height:8px;top:2px;left:-12px}
.card{left:342px;top:69px;width:844px;height:251px;background:var(--white);border:1px solid #cfd6dc}
.title{left:25px;top:11px;font-size:19px;color:#333}
.when{left:25px;top:37px;font-size:12px;color:#333}
.rule{left:15px;top:60px;width:812px;height:1px;background:#cfd3d7}
.share{left:738px;top:13px;width:76px;height:24px;border:1px solid #c9ccd0;background:#e9ebee;color:var(--muted);font-size:12px;padding:3px 0 0 36px}
.share svg{position:absolute;left:10px;top:4px}
.addr{left:25px;top:81px;font-size:12px;line-height:17px}
.desc{left:25px;top:149px;width:780px;font-size:12px;line-height:17px}
.btn-view{left:25px;top:208px;width:110px;height:24px;border:1px solid #c9ccd0;background:#f0f1f3;font-size:12px;padding:3px 0 0 27px}
.btn-view svg{position:absolute;left:8px;top:4px}
.btn-pdf{left:865px;top:334px;width:175px;height:24px;background:var(--green);color:#fff;font-size:12px;padding:3px 0 0 25px}
.btn-pdf svg{position:absolute;left:8px;top:4px}
.btn-print{left:1047px;top:334px;width:129px;height:24px;border:1px solid #c9ccd0;background:#eceef1;color:var(--muted);font-size:12px;padding:3px 0 0 28px}
.btn-print svg{position:absolute;left:7px;top:4px}
</style>
</head>
<body>
<header class="abs topbar">
  <div class="abs brand">ESD</div>
  <nav class="nav">
    <a style="left:800px">FEATURED</a>
    <a class="active" style="left:905px">MEETINGS</a>
    <a style="left:1011px">AGENDA</a>
    <a style="left:1108px">POLICIES</a>
  </nav>
</header>

<aside class="abs sidebar"></aside>
<div class="abs divider"></div>

<div class="abs search">
  <svg width="14" height="14" viewBox="0 0 14 14"><circle cx="6" cy="6" r="4.8" fill="none" stroke="#666" stroke-width="1.4"/><line x1="9.5" y1="9.5" x2="13" y2="13" stroke="#666" stroke-width="1.4"/></svg>
  Search meetings by Month, Date or Year
</div>
<div class="abs featured">Featured<span>+</span></div>
<div class="abs featured-list"></div>

<section class="abs calendar">
  <svg class="abs" style="left:28px;top:31px" width="18" height="12" viewBox="0 0 18 12"><path d="M17 6H2M7 1L2 6l5 5" fill="none" stroke="#0b6a2c" stroke-width="1.5"/></svg>
  <div class="abs year">2025</div>
  <svg class="abs" style="left:241px;top:31px" width="18" height="12" viewBox="0 0 18 12"><path d="M1 6h15M11 1l5 5-5 5" fill="none" stroke="#0b6a2c" stroke-width="1.5"/></svg>
  <div class="abs months">
    <span style="left:43px">FEB</span><span style="left:85px">MAR</span><span class="cur" style="left:127px">APR</span><span style="left:173px">MAY</span><span style="left:219px">JUN</span>
  </div>
  <div class="dow">
    <span style="left:37px">Su</span><span style="left:73px">Mo</span><span style="left:110px">Tu</span><span style="left:146px">We</span><span style="left:182px">Th</span><span style="left:217px">Fr</span><span style="left:250px">Sa</span>
  </div>
  <div class="days">
    <span style="left:146px;top:137px">1</span><span style="left:182px;top:137px">2</span><span style="left:217px;top:137px">3</span><span style="left:250px;top:137px">4</span>
    <span style="left:37px;top:164px">5</span><span style="left:73px;top:164px">6</span><span style="left:110px;top:164px">7</span><span style="left:146px;top:164px">8</span><span style="left:182px;top:164px">9</span><span style="left:217px;top:164px">10</span><span style="left:250px;top:164px">11</span>
    <span style="left:37px;top:191px">12</span><span style="left:73px;top:191px">13</span><span style="left:110px;top:191px">14</span><span style="left:146px;top:191px">15</span><span style="left:182px;top:191px">16</span><span style="left:217px;top:191px">17</span><span style="left:250px;top:191px">18</span>
    <span style="left:37px;top:218px">19</span><span style="left:73px;top:218px">20</span><span style="left:110px;top:218px">21</span><span style="left:146px;top:218px">22</span><span style="left:182px;top:218px">23</span><span class="sel" style="left:216px;top:215px">24</span><span style="left:250px;top:218px">25</span>
    <span style="left:37px;top:245px">26</span><span style="left:73px;top:245px">27</span><span style="left:110px;top:245px">28</span><span style="left:146px;top:245px">29</span><span style="left:182px;top:245px">30</span><span style="left:217px;top:245px">31</span>
  </div>
  <i class="dot" style="left:145px;top:150px;background:var(--green)"></i>
  <i class="dot" style="left:216px;top:177px;background:var(--green)"></i>
  <i class="dot" style="left:37px;top:231px;background:var(--red)"></i>
</section>

<div class="abs legend" style="left:48px;top:626px"><i class="dot" style="background:var(--gold);border-radius:0;clip-path:polygon(50% 0,61% 38%,100% 38%,69% 61%,80% 100%,50% 76%,20% 100%,31% 61%,0 38%,39% 38%)"></i>Specialised Meetings</div>
<div class="abs legend" style="left:188px;top:626px"><i class="dot" style="background:var(--red)"></i>Cancelled Meetings</div>
<div class="abs legend" style="left:48px;top:644px"><i class="dot" style="background:var(--green)"></i>Regular Meetings</div>

<main class="abs card">
  <h1 class="abs title" style="font-weight:400">Regular Meeting Agenda</h1>
  <p class="abs when">6:00 P.M, Thursday, April 24, 2025</p>
  <div class="abs share">
    <svg width="16" height="15" viewBox="0 0 16 15"><circle cx="3" cy="7.5" r="2.6" fill="#9aa0a6"/><circle cx="13" cy="2.8" r="2.6" fill="#9aa0a6"/><circle cx="13" cy="12.2" r="2.6" fill="#9aa0a6"/><path d="M3 7.5L13 2.8M3 7.5l10 4.7" stroke="#9aa0a6" stroke-width="1.4"/></svg>
    Share
  </div>
  <div class="abs rule"></div>
  <address class="abs addr" style="font-style:normal">Brookfield High School Media Center<br>1800 East Maple Ridge Road<br>Elmwood, Ohio, 44120</address>
  <p class="abs desc">This meeting is a meeting of the Board of Education in public for the purpose of conducting the District's business. There is a time for public participation during the meeting as indicated in the agenda.</p>
  <div class="abs btn-view">
    <svg width="13" height="15" viewBox="0 0 13 15"><rect x="1" y="1" width="11" height="13" fill="none" stroke="#0b6a2c" stroke-width="1.2"/><path d="M3 5h7M3 8h7M3 11h5" stroke="#0b6a2c" stroke-width="1.2"/></svg>
    View Agenda
  </div>
</main>

<div class="abs btn-pdf">
  <svg width="12" height="15" viewBox="0 0 12 15"><path d="M1 1h7l3 3v10H1z" fill="none" stroke="#fff" stroke-width="1.1"/><path d="M3.5 11c2-4 3-6 2-7s-1 3 3 6" fill="none" stroke="#fff" stroke-width=".9"/></svg>
  Download Agenda as PDF
</div>
<div class="abs btn-print">
  <svg width="16" height="15" viewBox="0 0 16 15"><rect x="4" y="1" width="8" height="4" fill="#666"/><rect x="1" y="5" width="14" height="6" rx="1" fill="#666"/><rect x="4" y="9" width="8" height="5" fill="#fff" stroke="#666"/></svg>
  Print the Agenda
</div>

<svg class="abs" style="left:447px;top:406px" width="12" height="19" viewBox="0 0 12 19"><path d="M2 2l7.5 7.5L2 17" fill="none" stroke="#111" stroke-width="2.6"/></svg>
</body>
</html>
```